Website and Logo Design for new niche job board.

Hello, We are an up and coming job board that is focused on LEGITIMATE companies that hire telecommuters to work from home. We are looking to build a highly interactive job board and forum/blog. The site is called WorkHarbor.com We focus on helping work at home moms, older workers and college students in work at home positions. We offer free job posting and advertising to the employer and free resume posting to the job seeker. (Free everything basically) Our revenue will be based from banner ads on the site so we will need a space on both sides of the page for those ads. 

The software we are using to build the job board part of the site can be viewed at www.pavloquill.example. It is already built! We do not need job software but a dashboard look to our main page - PLEASE pay attention to this! Do not submit a job board look as we have the job board page built!

These are the sites I like - please use these links to understand exactly the look I want

 

http://www.brightmarmots.example/

http://www.tessvoran.example/

http://www.ladiesatlabor.example/

https://www.findingnannies.example/index.asp?
Updates

Hi everyone- I think there might be some confusion to what we are looking for. We have the job board software through www.pavloquill.example, we are looking for the main page to be built around that. Basically we want a dashboard look with lots of little boxes to add content such as different articles,podcasts, forums,blogs,highlight different companies hiring,etc. If you can add scrolling or moving objects would be ideal. The less of a static website the better. You dont have to worry about the jobboard portion just the main page when you click on www.WorkHarbor.com, we really need it to capture peoples attention and see its a staffing firm AND a job board, forum, etc for work at home positions.  Here are some looks I am aiming for -

http://www.tessvoran.example/

Please use alot of color- lime green, oranges, turquiose blue, purple, lots and lots of color please! I like more tropical colors. Thanks! I dont like red and dark colors at all. Thanks

Target Market(s)

Target customers will be both companies and individuals. The individuals will be a broad age range that are interested in working from home. The companies will be small to large corporations that have valid work from home positions.

Requirements
Must have
• I want a colorful site with moving objects and scrolling text - static sites are bland, and outdated- I am looking for a HIGHLY interactive board. Please do not just throw a template up there and expect me to like it. I am picky and want an ultra sleek design and eye catching. I can make an out of the box website myself, I have 3 other companies and did that -  PLEASE PLEASE DO NOT SHOW ME A COOKIE!
Nice to have
• Would be very nice to have the HTML sliced up for finished designs.
Should not have
• just not boring and static. Anything new and creative is where we are heading.

```html
<!DOCTYPE html>
<html lang="en">
<head>
<meta charset="utf-8">
<title>WorkHarbor.com – Job Board and Forum/Blog</title>
<link rel="stylesheet" href="https://fonts.googleapis.com/css2?family=Source+Sans+3:wght@400;600;700&family=Noto+Sans:wght@400;700&display=swap">
<style>
:root{
  --ink:#333333;
  --muted:#6b6b6b;
  --logo-blue:#1f5c96;
  --panel-head:#6a6a6a;
  --panel-border:#b9b9b9;
  --rule:#9a9a9a;
  --orange:#f47a12;
  --orange-light:#ffae5c;
  --sky:#1d8fd0;
  --sky-light:#4fb3e8;
  --lime:#c7d92a;
  --lime-light:#e3ec5a;
  --cell:#e6e6e6;
  --cell-dark:#bdbdbd;
  --btn-grey:#555555;
  --btn-blue:#3a8fcf;
  --link-orange:#f28a1c;
  --link-green:#4a8f00;
  --white:#ffffff;
}
*{box-sizing:border-box;margin:0;padding:0}
html,body{width:1200px;height:945px;overflow:hidden;background:var(--white)}
body{position:relative;font-family:"Source Sans 3",Arial,sans-serif;color:var(--ink)}
.abs{position:absolute}

/* header */
.logo{left:41px;top:28px}
.logo-name{font-size:38px;font-weight:400;color:var(--logo-blue);letter-spacing:-1px;line-height:1}
.logo-tag{font-size:12px;font-weight:600;color:var(--muted);margin-top:4px;letter-spacing:.3px}
.affiliate{left:480px;top:12px;width:683px;height:75px;border:1px solid #2a7fb5;
  background:linear-gradient(90deg,#1b8ccc,#5cc3ee 60%,#a8e0f7);color:var(--white);overflow:hidden}
.affiliate h2{position:absolute;left:18px;top:2px;font-family:"Noto Sans",Arial,sans-serif;font-size:34px;font-weight:700}
.affiliate p{position:absolute;left:370px;top:40px;font-family:"Noto Sans",Arial,sans-serif;font-size:28px;font-weight:700}
.affiliate .device{position:absolute;right:14px;top:4px;width:150px;height:66px;background:linear-gradient(160deg,#3b3b3b,#8a9aa8);border-radius:3px}
.top-rule{left:33px;top:112px;width:1134px;height:2px;background:var(--rule)}

/* panels */
.panel{border:1px solid var(--panel-border);border-radius:6px;background:var(--white);overflow:hidden}
.panel-head{height:31px;background:var(--panel-head);color:var(--white);font-size:16px;font-weight:700;
  letter-spacing:-.3px;padding:6px 12px;text-transform:uppercase;border-radius:5px 5px 0 0}

.search{left:34px;top:123px;width:302px;height:185px}
.field-row{display:flex;align-items:center;justify-content:space-between;margin:0 14px 0 18px;height:37px;border-bottom:1px dotted #c8c8c8}
.field-row:last-of-type{border-bottom:none}
.field-row label{font-size:10px;font-weight:600;color:var(--muted)}
.field-row span.input{width:128px;height:25px;border:1px solid #a8a8a8;background:var(--white)}
.btn-grey{position:absolute;right:10px;bottom:8px;width:76px;height:24px;background:var(--btn-grey);color:var(--white);
  font-size:11px;font-weight:600;text-align:center;line-height:24px;border-radius:2px}

.hero{left:347px;top:123px;width:589px;height:185px;border-radius:6px;overflow:hidden;
  background:linear-gradient(90deg,#1677b8,#3ea0dc 55%,#8cc9ec)}
.hero-photo{position:absolute;right:0;top:0;width:215px;height:185px;background:linear-gradient(135deg,#d9e6ef,#8fa9bd 60%,#5a6f84)}
.hero h1{position:absolute;left:40px;top:36px;font-family:"Noto Sans",Arial,sans-serif;font-size:21px;font-weight:700;color:var(--white)}
.hero ul{position:absolute;left:40px;top:72px;list-style:none;font-family:"Noto Sans",Arial,sans-serif;font-size:14px;color:var(--white);line-height:16px}
.hero li{margin-bottom:10px;padding-left:14px;position:relative}
.hero li::before{content:"";position:absolute;left:0;top:4px;border-left:6px solid var(--white);border-top:4px solid transparent;border-bottom:4px solid transparent}
.hero b{font-weight:700;text-transform:uppercase}

.follow{left:948px;top:123px;width:211px;height:185px}
.social{position:absolute;width:58px;height:58px;border-radius:10px}

/* nav */
.nav{left:32px;top:318px;width:1135px;height:39px;background:linear-gradient(180deg,var(--orange-light),var(--orange) 55%,#e86a05);
  border-radius:0 6px 0 0}
.nav ul{position:absolute;left:309px;top:0;display:flex;list-style:none;height:39px;align-items:center}
.nav li{color:var(--white);font-family:"Noto Sans",Arial,sans-serif;font-size:15px;font-weight:700;padding:0 15px;border-right:1px solid #ffb877;line-height:24px}
.nav li:last-child{border-right:none}
.nav li.current{text-decoration:underline;text-underline-offset:4px}
.site-search{position:absolute;left:845px;top:9px;display:flex;align-items:center;gap:10px}
.site-search label{font-family:"Noto Sans",Arial,sans-serif;font-size:9px;font-weight:700;color:#222}
.site-search .input{width:142px;height:23px;background:var(--white);border:1px solid #d98a3a}
.btn-blue{background:var(--btn-blue);color:var(--white);font-size:13px;font-weight:700;text-align:center;border-radius:3px}
.site-search .btn-blue{width:36px;height:24px;line-height:24px}

/* login */
.login{left:34px;top:367px;width:302px;height:116px;background:#ededed}
.login .panel-head::after{content:"";position:absolute;right:14px;top:12px;border-left:5px solid var(--white);border-top:4px solid transparent;border-bottom:4px solid transparent}
.login .panel-head{position:relative}
.login-fields{position:relative;padding:8px 12px 0 22px}
.login-fields .col{position:absolute;top:8px;font-size:9px;font-weight:600;color:var(--muted)}
.login-fields .col span.input{display:block;width:127px;height:24px;border:1px solid #a8a8a8;background:var(--white);margin-top:4px}
.login-foot{position:absolute;top:86px;font-size:9px;font-weight:600;color:var(--muted)}
.login-foot a{color:var(--logo-blue);text-decoration:none;font-weight:700}
.login .btn-blue{position:absolute;right:12px;top:84px;width:34px;height:22px;line-height:22px}

/* comments */
.comments{left:34px;top:507px;width:302px;height:288px}
.comments .body{padding:12px 12px 0 12px;font-size:13px;line-height:18px;text-align:justify;color:#222}
.avatar{float:left;width:80px;height:84px;margin:0 8px 2px 0;border:1px solid #999;background:linear-gradient(160deg,#d7c3a4,#9b7a5a 60%,#5c4632)}
.read-more{color:var(--link-orange);float:right}

/* showcase */
.showcase{left:347px;top:367px;width:505px;height:445px}
.row{position:absolute;left:5px;height:68px;display:flex;gap:2px}
.cell{background:var(--cell);height:68px;font-family:"Noto Sans",Arial,sans-serif;font-size:12px;color:#222;display:flex;align-items:center;justify-content:center}
.cell.num{width:55px;font-weight:700}
.cell.subject{width:188px;display:block;padding:7px 6px;font-size:10.5px;line-height:15px}
.cell.subject strong{color:#000}
.cell.subject .muted{color:var(--muted)}
.cell.subject a{color:#000}
.cell.count{width:55px;font-weight:700}
.cell.count.dark{background:var(--cell-dark)}
.cell.date{width:131px;display:block;padding:18px 12px;font-size:11px;line-height:17px}
.cell.date strong{color:#000}
.cell.date a{color:#000;font-size:10.5px}
.pager{position:absolute;right:8px;bottom:8px;font-family:"Noto Sans",Arial,sans-serif;font-size:11px;font-weight:700;color:#000;word-spacing:2px}

/* right ads */
.gift{left:866px;top:369px;width:303px;height:134px;border-radius:8px;background:linear-gradient(135deg,#35a8e0,var(--sky) 60%,#1170ad);overflow:hidden}
.gift-box{position:absolute;left:18px;top:28px;width:72px;height:78px;background:linear-gradient(180deg,#e6d22a,#d4a10f);border-radius:3px}
.gift h3{position:absolute;left:115px;top:26px;font-size:36px;line-height:38px;font-weight:700;color:var(--white)}
.gift span{position:absolute;right:22px;top:104px;font-size:14px;font-weight:700;color:#0b2a45}
.fruits{left:866px;top:517px;width:303px;height:284px;border-radius:8px;background:radial-gradient(circle at 50% 40%,var(--lime-light),var(--lime) 70%,#a9bd12);overflow:hidden}
.fruits h3{position:absolute;left:30px;top:20px;font-size:52px;font-weight:400;letter-spacing:-1.5px;color:#f6f35a}
.fruits h3 b{font-weight:400;color:var(--white)}
.fruits p{position:absolute;left:138px;top:104px;font-size:14px;line-height:16px;font-weight:700;color:var(--white);text-transform:uppercase}
.basket{position:absolute;left:0;top:132px;width:130px;height:120px;border-radius:40% 50% 10% 10%;background:linear-gradient(180deg,#b6413a,#8a5a2c 55%,#6b4321)}
.fruits a{position:absolute;right:22px;bottom:24px;color:var(--white);font-size:16px;font-weight:700}

/* footer */
.foot-band{left:32px;top:821px;width:1135px;height:14px;background:#b0b0b0}
.foot-links{left:0;top:850px;width:1200px;text-align:center;font-size:13px;color:#444}
.foot-links span{padding:0 8px;border-right:1px solid #444}
.foot-links span:last-child{border-right:none}
.copyright{left:0;top:881px;width:1200px;text-align:center;font-size:13px;color:#444}
.legal{left:0;top:904px;width:1200px;text-align:center;font-size:13px;color:#444}
.legal a{color:var(--link-green);padding:0 6px}
</style>
</head>
<body>

<header class="abs logo">
  <div class="logo-name">WORKHARBOR.COM</div>
  <div class="logo-tag">JOB BOARD AND FORUM/BLOG</div>
</header>

<div class="abs affiliate">
  <h2>Join our affiliate program</h2>
  <p>SAVE 30%</p>
  <div class="device" role="img" aria-label="Laptop computer"></div>
</div>
<div class="abs top-rule"></div>

<section class="abs panel search">
  <div class="panel-head">Search Projects</div>
  <div style="padding-top:4px">
    <div class="field-row"><label>BROWS BY CATEGORY</label><span class="input"></span></div>
    <div class="field-row"><label>BROWS BY CITY</label><span class="input"></span></div>
    <div class="field-row"><label>BROWS BY PRICE</label><span class="input"></span></div>
  </div>
  <div class="btn-grey">SEARCH</div>
</section>

<section class="abs hero">
  <div class="hero-photo" role="img" aria-label="Two business colleagues working at a computer"></div>
  <h1>WE ENSURE YOUR SUCCESS!</h1>
  <ul>
    <li><b>Managing</b><br>your time more productively.</li>
    <li><b>Focusing</b> more clearly<br>on what is most important to<br>your business.</li>
  </ul>
</section>

<section class="abs panel follow">
  <div class="panel-head">Follow Us</div>
  <div class="social" style="left:30px;top:44px;background:#f58a1f"></div>
  <div class="social" style="left:117px;top:44px;background:#1d4f9a"></div>
  <div class="social" style="left:30px;top:115px;background:#38b6e8"></div>
  <div class="social" style="left:117px;top:115px;background:#3a5ba0"></div>
</section>

<nav class="abs nav">
  <ul>
    <li class="current">Home</li>
    <li>About us</li>
    <li>Support</li>
    <li>Clients</li>
    <li>Contact</li>
  </ul>
  <div class="site-search">
    <label>WEBSITE SEARCH</label>
    <span class="input"></span>
    <span class="btn-blue">GO</span>
  </div>
</nav>

<section class="abs panel login">
  <div class="panel-head">Login</div>
  <div class="login-fields">
    <div class="col" style="left:22px">LOGN NAME<span class="input"></span></div>
    <div class="col" style="left:163px">PASSWORD<span class="input"></span></div>
  </div>
  <div class="login-foot" style="left:22px">NEW USER <a>SIGNUP NOW!</a></div>
  <div class="login-foot" style="left:153px">FORGOTE PASSWORD?</div>
  <div class="btn-blue">OK</div>
</section>

<section class="abs panel comments">
  <div class="panel-head">Member's Comments.</div>
  <div class="body">
    <div class="avatar" role="img" aria-label="Member portrait photo"></div>
    Spring has sprung and the sun is out! As the gorgeous weather sets in and bikini season looms overhead, most of us are probably thinking, “It’s time to hit the gym.” Before your Spring has sprung and the sun is out! As the gorgeous weather sets in and bikini season looms overhead, most of us are probably thinking, “It’s time to hit the gym.” Before your bikini<br><br>
    are probably thinking, “It’s time to hit the gym.” Before your bitnes <span class="read-more">....Read More</span>
  </div>
</section>

<section class="abs panel showcase">
  <div class="panel-head" style="border-radius:5px 5px 0 0">Project Showcase</div>
  <div class="row" style="top:45px">
    <div class="cell num">01</div>
    <div class="cell subject"><strong>Subject - &nbsp;tempor invidunt ut</strong><br><span class="muted">abore Lorem conseter dolor sit</span><br>Moderator: <a>Administrator</a></div>
    <div class="cell count">18</div><div class="cell count dark">18</div>
    <div class="cell date"><strong>August 09, 2006</strong><br><a>membername link</a></div>
  </div>
  <div class="row" style="top:120px">
    <div class="cell num">01</div>
    <div class="cell subject"><strong>Subject - &nbsp;tempor invidunt ut</strong><br><span class="muted">abore Lorem conseter dolor sit</span><br>Moderator: <a>Administrator</a></div>
    <div class="cell count">18</div><div class="cell count dark">18</div>
    <div class="cell date"><strong>August 09, 2006</strong><br><a>membername link</a></div>
  </div>
  <div class="row" style="top:195px">
    <div class="cell num">01</div>
    <div class="cell subject"><strong>Subject - &nbsp;tempor invidunt ut</strong><br><span class="muted">abore Lorem conseter dolor sit</span><br>Moderator: <a>Administrator</a></div>
    <div class="cell count">18</div><div class="cell count dark">18</div>
    <div class="cell date"><strong>August 09, 2006</strong><br><a>membername link</a></div>
  </div>
  <div class="row" style="top:270px">
    <div class="cell num">01</div>
    <div class="cell subject"><strong>Subject - &nbsp;tempor invidunt ut</strong><br><span class="muted">abore Lorem conseter dolor sit</span><br>Moderator: <a>Administrator</a></div>
    <div class="cell count">18</div><div class="cell count dark">18</div>
    <div class="cell date"><strong>August 09, 2006</strong><br><a>membername link</a></div>
  </div>
  <div class="row" style="top:345px">
    <div class="cell num">01</div>
    <div class="cell subject"><strong>Subject - &nbsp;tempor invidunt ut</strong><br><span class="muted">abore Lorem conseter dolor sit</span><br>Moderator: <a>Administrator</a></div>
    <div class="cell count">18</div><div class="cell count dark">18</div>
    <div class="cell date"><strong>August 09, 2006</strong><br><a>membername link</a></div>
  </div>
  <div class="pager">Page : &nbsp;01 | 02 | 03 | 04 | 05 ....Next</div>
</section>

<aside class="abs gift">
  <div class="gift-box" role="img" aria-label="Wrapped gift box with green ribbon"></div>
  <h3>SPECIAL<br>GIFT</h3>
  <span>CLICK HERE</span>
</aside>

<aside class="abs fruits">
  <h3><b>Fresh</b>Fruits</h3>
  <p>We use only<br>the best ingredients</p>
  <div class="basket" role="img" aria-label="Basket of fresh fruit"></div>
  <a>read more</a>
</aside>

<div class="abs foot-band"></div>
<footer>
  <div class="abs foot-links"><span>Home</span><span>About Us</span><span>Projects</span><span>Feredbacks</span><span>Support</span><span>Contacts</span><span>Help</span><span>Sitemap</span></div>
  <div class="abs copyright">Copyright © Companyname, 2006. All Rights Reserved</div>
  <div class="abs legal"><a>Privacy Policy</a>|<a>User Agreement</a>|<a>Copyright Info</a></div>
</footer>

</body>
</html>
```